Business card for Bio pharmaceutical company

Hello,
We are a bio pharmaceutical contract manufacturing company in Brisbane, Australia. Can you please create a new business card design. Please go to our website for colours http://www.veltromedix.com.au.
On the back can you include the cartoon mascot Tobi Warn and the tagline
"A Global Biopharmaceutical Contract Development Manufacturing Company"
Target Market(s)
Biotechnology
Industry/Entity Type
Pharmaceutical
Contact Information for Business Card
Karen Holbrooke
Business Development Manager
karen.holbrooke@veltromedix.com.au
1937 Mulgrave Street Kelby Queesnland 4076 Australia
T: +61 7 3591 6042
M +61 427 516 908
F +61 7 3648 2095
www.veltromedix.com.au

```html
<!DOCTYPE html>
<html lang="en">
<head>
<meta charset="utf-8">
<title>Veltromedix Business Card</title>
<link href="https://fonts.googleapis.com/css2?family=Exo+2:wght@400;600&family=Michroma&display=swap" rel="stylesheet">
<style>
  :root {
    --page-bg: #c9cbcc;
    --card-white: #ffffff;
    --brand-blue: #0f5078;
    --brand-green: #b5cf3a;
    --text-light: #ffffff;
    --divider: rgba(255,255,255,0.6);
  }
  * { margin: 0; padding: 0; box-sizing: border-box; }
  html, body { width: 1200px; height: 771px; overflow: hidden; }
  body {
    background: var(--page-bg);
    position: relative;
    font-family: "Exo 2", sans-serif;
  }
  .card {
    position: absolute;
    top: 235px;
    width: 520px;
    height: 300px;
    background: var(--card-white);
    box-shadow: 0 6px 18px rgba(0,0,0,0.18);
    overflow: hidden;
  }
  .card--logo { left: 60px; }
  .card--contact { left: 620px; }

  .brand {
    position: absolute;
    display: flex;
    align-items: center;
    gap: 12px;
  }
  .brand__name {
    font-family: "Exo 2", sans-serif;
    font-weight: 600;
    color: var(--brand-blue);
    letter-spacing: -0.5px;
  }
  .brand__mark { background: var(--brand-green); }
  .card--logo .brand { left: 34px; bottom: 70px; }
  .card--logo .brand__name { font-size: 40px; }
  .card--logo .brand__mark { width: 24px; height: 24px; }

  .tagline {
    position: absolute;
    left: 36px;
    bottom: 44px;
    font-size: 11px;
    letter-spacing: 0.4px;
    color: var(--brand-blue);
  }

  .card--contact .brand { right: 40px; top: 58px; }
  .card--contact .brand__name { font-size: 30px; }
  .card--contact .brand__mark { width: 18px; height: 18px; }

  .band {
    position: absolute;
    left: 0; top: 0;
    width: 520px; height: 300px;
  }
  .band__accent { fill: var(--brand-green); }
  .band__base { fill: var(--brand-blue); }

  .person {
    position: absolute;
    right: 270px;
    top: 198px;
    text-align: right;
    color: var(--text-light);
  }
  .person__name {
    font-family: "Michroma", sans-serif;
    font-size: 10px;
    letter-spacing: 1.5px;
    text-transform: uppercase;
  }
  .person__title {
    font-size: 9px;
    letter-spacing: 0.8px;
    margin-top: 3px;
  }
  .person__address {
    font-size: 9px;
    letter-spacing: 0.8px;
    margin-top: 8px;
    line-height: 1.45;
  }
  .divider {
    position: absolute;
    left: 262px;
    top: 198px;
    width: 1px;
    height: 78px;
    background: var(--divider);
  }
  .contacts {
    position: absolute;
    left: 274px;
    top: 198px;
    list-style: none;
    color: var(--text-light);
    font-size: 9.5px;
    letter-spacing: 0.8px;
  }
  .contacts li {
    display: flex;
    align-items: center;
    gap: 6px;
    height: 15.5px;
    white-space: nowrap;
  }
  .contacts svg { width: 10px; height: 10px; flex: none; }
  .icon-bg { fill: var(--text-light); }
  .icon-glyph { fill: var(--brand-blue); }
</style>
</head>
<body>

  <section class="card card--logo">
    <div class="brand">
      <span class="brand__name">Veltromedix</span>
      <span class="brand__mark"></span>
    </div>
    <p class="tagline">A Global Biopharmaceutical Contract Development Manufacturing Company</p>
  </section>

  <section class="card card--contact">
    <div class="brand">
      <span class="brand__name">Veltromedix</span>
      <span class="brand__mark"></span>
    </div>

    <svg class="band" viewBox="0 0 520 300" aria-hidden="true">
      <path class="band__accent" d="M0 112 C 140 98, 300 178, 520 150 L520 300 L0 300 Z"/>
      <path class="band__base" d="M0 132 C 150 114, 300 192, 520 166 L520 300 L0 300 Z"/>
    </svg>

    <div class="person">
      <p class="person__name">Karen Holbrooke</p>
      <p class="person__title">Business Development Manager</p>
      <p class="person__address">1937 Mulgrave Street<br>Kelby Queesnland 4076<br>Australia</p>
    </div>

    <div class="divider"></div>

    <ul class="contacts">
      <li>
        <svg viewBox="0 0 10 10"><circle class="icon-bg" cx="5" cy="5" r="5"/><path class="icon-glyph" d="M3 2.5 L4.2 2.5 L4.6 4 L4 4.6 Q4.6 5.6 5.4 6 L6 5.4 L7.5 5.8 L7.5 7 Q4.5 7.2 3 2.5Z"/></svg>
        <span>+61 7 3591 6042</span>
      </li>
      <li>
        <svg viewBox="0 0 10 10"><circle class="icon-bg" cx="5" cy="5" r="5"/><rect class="icon-glyph" x="3.5" y="2" width="3" height="6" rx="0.6"/></svg>
        <span>+61 427 516 908</span>
      </li>
      <li>
        <svg viewBox="0 0 10 10"><circle class="icon-bg" cx="5" cy="5" r="5"/><rect class="icon-glyph" x="2.5" y="4" width="5" height="3.2"/><rect class="icon-glyph" x="3.5" y="2.5" width="3" height="1.2"/></svg>
        <span>+61 7 3648 2095</span>
      </li>
      <li>
        <svg viewBox="0 0 10 10"><circle class="icon-bg" cx="5" cy="5" r="5"/><rect class="icon-glyph" x="2.4" y="3.2" width="5.2" height="3.6"/></svg>
        <span>karen.holbrooke@veltromedix.com.au</span>
      </li>
      <li>
        <svg viewBox="0 0 10 10"><circle class="icon-bg" cx="5" cy="5" r="5"/><circle class="icon-glyph" cx="5" cy="5" r="2.6"/></svg>
        <span>www.veltromedix.com.au</span>
      </li>
    </ul>
  </section>

</body>
</html>
```